Postcard for our major fundraising event - LiftingSTAR2018

Bright Meadow KIDS Camp (BMK) and Youth Trail Pathway Camp (YTPC) are ministries of Larkfield Gospel Church that serve Ventura County children of abuse, abandonment and neglect living in foster care. We are looking for a postcard design to promote our single largest fundraising event of the year, NurturingSTAR2018, to raise awareness and support for children of abuse. NurturingSTAR is a dinner banquet on at an exclusive outdoor venue, "Willow Hollow" with a rustic, ranch feel and with spectacular panoramic views of the City of Camarillo. The event will include music, refreshments, appetizers, a Santa Maria-style barbeque (BBQ), coffee and dessert, testimonials from camp, prize drawings, an opportunity to partner with BMK and YTPC, and time to socialize before and after.
Updates

I have just uploaded text copy to help designers come closer to what we are looking for. Thank you very much for your interest! -Dale

Target Market(s)

People from both within and from outside our sponsoring church who have a heart for hurting children and who are willing and able to financially support our camping (BMK & YTPC) ministries.

Industry/Entity Type

Church

Font styles to use
Serif
Decorative
Script

Requirements
Must have
• Name: NurturingSTAR2018... raising awareness and support for children of abuse
• Date: Thursday, May 24, 2018, 6:30-8:00 pm
• Place: Willow Hollow at Marlowe Ranch, 7100 Quillan Road, Somis, California.
• Cost: $30 per person
• Tickets: Available at Ticketmill.example
• Front side should include the elements of the event (although not necessarily bulleted like below):
• • Social hour
• • Music
• • Hors d’eourves
• • Refreshments
• • Santa Maria-style BBQ dinner
• • Coffee & dessert
• • Prize drawings
• • Stories from camp
• See attachment for suggested copy for back side.
• BMK and YTPC logos should be included on the postcard. I’ve uploaded a variety of photos for the designer to choose from; they do not necessarily all have to be included. There are also lots more pics available on our Gatherbook (Bright Meadow KIDS of Ventura).
• The front-side of the postcard can be entirely images and text. The back-side of the post card should include our return address at the top left ("BMK/YTPC of Larkfield Gospel Church, 820 Fernbrook Lane, Ventura, CA 93003") and should leave at least the right half of the postcard clear for addressing and postage.
• BMK colors are purple (Pantone 267) and red (Pantone 186). YTPC colors are green and yellow.
Nice to have
• A selection of camp photos large enough to easily view, but no so many that they are too small to identify. And, perhaps, a design element that evokes a rustic, outdoors, western, ranch feel, but not so much that it seems that we are promoting a country hoedown.
Should not have
• Anything sexual or sensual, related to alcoholic beverages, gambling, guns, or anything negative.

```html
<!DOCTYPE html>
<html lang="en">
<head>
<meta charset="utf-8">
<title>NurturingSTAR 2018 Postcard</title>
<link rel="stylesheet" href="https://fonts.googleapis.com/css2?family=Montserrat:wght@400;500;600;700&display=swap">
<style>
:root{
  --purple:#2f2466;
  --red:#d3202a;
  --ink:#2b2b33;
  --white:#ffffff;
  --rule:#b9b9bf;
  --stage:#e9e6e2;
  --stamp:#dcdcde;
}
*{box-sizing:border-box;margin:0;padding:0}
html,body{width:1200px;height:903px;overflow:hidden;background:var(--stage);font-family:'Montserrat',sans-serif;color:var(--ink)}
.postcard{position:absolute;background:var(--white);box-shadow:0 4px 14px rgba(0,0,0,.18);overflow:hidden}
.front{left:114px;top:82px;width:582px;height:376px}
.back{left:504px;top:472px;width:582px;height:376px}
.photo-strip{position:absolute;left:0;top:0;width:582px;height:192px}
.title{position:absolute;left:0;width:100%;top:186px;text-align:center;font-size:29px;line-height:34px;font-weight:700;color:var(--purple);letter-spacing:-.2px}
.title .accent{color:var(--red)}
.tagline{position:absolute;left:0;width:100%;top:220px;text-align:center;font-size:11px;line-height:14px;color:var(--ink)}
.date-bar{position:absolute;left:129px;top:237px;width:325px;height:22px;background:var(--red);border-radius:3px;color:var(--white);font-size:16px;text-align:center;line-height:22px}
.event-list{position:absolute;left:40px;top:263px;width:502px;text-align:center;font-size:9px;line-height:12px;color:var(--purple);font-weight:500}
.event-list .sep{color:var(--red);padding:0 3px}
.brand-left{position:absolute;left:22px;top:208px;width:100px;font-size:13px;font-weight:700;color:var(--purple);line-height:1.15;text-align:center}
.brand-right{position:absolute;left:482px;top:214px;display:flex;align-items:center;gap:5px;font-size:12px;font-weight:700;color:var(--purple)}
.brand-right .dot{width:20px;height:20px;border-radius:50%;background:#2e8b3a}
.info-box{position:absolute;top:302px;height:34px;border:1px solid var(--rule);border-radius:3px;display:flex;align-items:center;justify-content:center;text-align:center;color:var(--purple);white-space:nowrap}
.info-box .label{position:absolute;top:-7px;left:50%;transform:translateX(-50%);background:var(--white);padding:0 4px;font-size:10.5px;font-weight:600;color:var(--red);letter-spacing:.3px;line-height:12px}
.place{left:14px;width:212px;font-size:10.5px;line-height:13px;padding-top:3px}
.cost{left:234px;width:140px;font-size:16px;padding-top:3px}
.cost strong{color:var(--red);font-weight:700}
.tickets{left:382px;width:186px;font-size:10.5px;padding-top:3px}
.contact-band{position:absolute;left:0;top:344px;width:582px;height:32px;background:var(--purple);display:flex;align-items:center;justify-content:center;gap:24px;color:var(--white);font-size:10.5px}
.contact-band span{display:flex;align-items:center;gap:6px}
.return-address{position:absolute;left:28px;top:30px;font-size:8.5px;line-height:10.4px;color:var(--ink);font-style:normal}
.stamp-box{position:absolute;left:502px;top:27px;width:57px;height:67px;background:var(--stamp)}
.address-line{position:absolute;left:316px;width:243px;height:1px;background:var(--rule)}
</style>
</head>
<body>
<section class="postcard front">
  <svg class="photo-strip" viewBox="0 0 582 192" width="582" height="192">
    <defs>
      <linearGradient id="park" x1="0" y1="0" x2="0" y2="1"><stop offset="0" stop-color="#1d2a14"/><stop offset="1" stop-color="#6f7a4a"/></linearGradient>
      <linearGradient id="banquet" x1="0" y1="0" x2="1" y2="1"><stop offset="0" stop-color="#7c8a54"/><stop offset="1" stop-color="#3f5a34"/></linearGradient>
      <linearGradient id="hats" x1="0" y1="0" x2="1" y2="1"><stop offset="0" stop-color="#d97aa8"/><stop offset="1" stop-color="#8a6a4a"/></linearGradient>
      <linearGradient id="craft" x1="0" y1="0" x2="1" y2="1"><stop offset="0" stop-color="#b8aa8a"/><stop offset="1" stop-color="#5d6070"/></linearGradient>
    </defs>
    <rect x="0" y="0" width="582" height="100" fill="url(#park)" role="img" aria-label="Campers riding horses along a shaded park trail"/>
    <path d="M0 78 Q291 132 582 78 L582 192 L0 192 Z" fill="#ffffff"/>
    <path d="M0 82 Q291 134 582 82" fill="none" stroke="#c9c9cc" stroke-width="1"/>
    <path d="M0 84 Q95 100 190 104 L190 182 L0 182 Z" fill="url(#banquet)" role="img" aria-label="Volunteers serving food at an outdoor camp banquet"/>
    <path d="M196 105 Q291 108 386 105 L386 182 L196 182 Z" fill="url(#hats)" role="img" aria-label="Two campers in pink sun hats smiling at a craft table"/>
    <path d="M392 104 Q487 100 582 84 L582 182 L392 182 Z" fill="url(#craft)" role="img" aria-label="Counselor helping a camper build a wooden toy"/>
    <path d="M0 186 Q291 176 582 186" fill="none" stroke="#c9c9cc" stroke-width="1"/>
  </svg>

  <div class="brand-left">Bright Meadow KIDS</div>
  <h1 class="title">Nurturing<span class="accent">STAR</span> 2018</h1>
  <p class="tagline">raising awareness and support for children of abuse</p>
  <div class="date-bar">Thursday, May 24, 2018, 6:30-8:00 pm</div>
  <div class="brand-right"><span class="dot"></span>YTPC</div>

  <p class="event-list">Social hour<span class="sep">•</span>Music<span class="sep">•</span>Hors d’oeuvres<span class="sep">•</span>Refreshments<span class="sep">•</span>Santa Maria-style BBQ dinner<br>Coffee &amp; dessert<span class="sep">•</span>Prize drawings<span class="sep">•</span>Stories from camp</p>

  <div class="info-box place"><span class="label">PLACE:</span>Willow Hollow at Marlowe Ranch,<br>7100 Quillan Road, Somis, California.</div>
  <div class="info-box cost"><span class="label">COST:</span><span><strong>$30</strong> per person</span></div>
  <div class="info-box tickets"><span class="label">TICKETS:</span>Available at Ticketmill.example</div>

  <div class="contact-band">
    <span><svg width="10" height="10" viewBox="0 0 24 24"><path d="M6.6 10.8a15 15 0 0 0 6.6 6.6l2.2-2.2c.3-.3.7-.4 1-.2 1.1.4 2.3.6 3.6.6.6 0 1 .4 1 1V20c0 .6-.4 1-1 1A17 17 0 0 1 3 4c0-.6.4-1 1-1h3.5c.6 0 1 .4 1 1 0 1.3.2 2.5.6 3.6.1.3 0 .7-.2 1z" fill="#e8515a"/></svg>714-555-0142</span>
    <span><svg width="11" height="8" viewBox="0 0 22 16"><rect x="0" y="0" width="22" height="16" rx="2" fill="#e8515a"/><path d="M1 1l10 8 10-8" fill="none" stroke="#2f2466" stroke-width="2"/></svg>office@brightmeadowkids.example</span>
    <span><svg width="10" height="10" viewBox="0 0 24 24"><circle cx="12" cy="12" r="10" fill="none" stroke="#e8515a" stroke-width="2.4"/><path d="M2 12h20M12 2c3 3 3 17 0 20M12 2c-3 3-3 17 0 20" fill="none" stroke="#e8515a" stroke-width="2"/></svg>www.bmk.example</span>
  </div>
</section>

<section class="postcard back">
  <address class="return-address">
    BMK/YTPC of<br>Larkfield Gospel Church,<br>820 Fernbrook Lane,<br>Ventura, CA 93003
  </address>
  <div class="stamp-box"></div>
  <div class="address-line" style="top:176px"></div>
  <div class="address-line" style="top:214px"></div>
  <div class="address-line" style="top:246px"></div>
</section>
</body>
</html>
```